Business Card Design Project

I need a business card designed that is clean, simple and elegant.
I am a fashion and advertising photographer based in Cape Town and Durban South Africa.
check out my website: www.marlowvance.co.za for ideas
Updates
Hi all,
Thanks for your submissions so far!
Please note:
I want no more than than black, white and/or grey to be used.
I don't want any photos used.
I would like the card to be double sided.
I would like to continue the design similar to the past ones Ive used.
I hope this helps, please send me further questions should you have any.
many thanks!
Marlow
Hi,
Please have a look at the jpg I loaded(called inspiration) which is the direction or inspiration I am aiming at.
Also PLEASE remember NO PHOTOS to be included on the card
many thanks!!
Target Market(s)
You can look at my site to get a better understanding of the audience:
www.marlowvance.co.za
Industry/Entity Type
Advertising
Requirements
Must have
- Clean design which can also be used for a watermark on photographs
perhaps black background with white text/grey
company called: Marlow Vance Photography
Nice to have
- below I have added logos that I have used in the past.
Should not have
- pictures of cameras
tacky elements

```html
<!DOCTYPE html>
<html lang="en">
<head>
<meta charset="utf-8">
<title>Marlow Vance Photography — Business Card</title>
<link rel="stylesheet" href="https://fonts.googleapis.com/css2?family=Cabin+Condensed:wght@400&family=Didact+Gothic&display=swap">
<style>
  :root {
    --page: #ffffff;
    --card: #000000;
    --name: #d9d9d9;
    --contact: #cfcfcf;
    --word-light: #a9a9a9;
    --word-mid: #8c8c8c;
    --word-dark: #707070;
  }
  html, body {
    margin: 0;
    padding: 0;
    width: 1200px;
    height: 900px;
    overflow: hidden;
    background: var(--page);
  }
  .canvas {
    position: relative;
    width: 1200px;
    height: 900px;
  }
  .business-card {
    position: absolute;
    left: 12px;
    top: 130px;
    width: 1176px;
    height: 650px;
    display: block;
    background: var(--card);
  }
  .wordmark {
    font-family: "Cabin Condensed", "Arial Narrow", sans-serif;
    font-weight: 400;
  }
  .wordmark-first { font-size: 182px; fill: var(--word-light); }
  .wordmark-last { font-size: 152px; fill: var(--word-mid); }
  .wordmark-trade { font-size: 84px; fill: var(--word-dark); letter-spacing: 2px; }
  .holder-name {
    font-family: "Didact Gothic", "Century Gothic", sans-serif;
    font-size: 40px;
    letter-spacing: 2px;
    fill: var(--name);
  }
  .contact-line {
    font-family: "Didact Gothic", "Century Gothic", sans-serif;
    font-size: 30px;
    fill: var(--contact);
  }
</style>
</head>
<body>
<main class="canvas">
  <svg class="business-card" viewBox="0 0 1176 650" width="1176" height="650" overflow="hidden" aria-label="Marlow Vance Photography business card">
    <rect width="1176" height="650" fill="var(--card)"/>

    <g class="wordmark wordmark-left" text-anchor="end">
      <text class="wordmark-first" x="268" y="286">MARLOW</text>
      <text class="wordmark-last" x="268" y="450">VANCE</text>
      <text class="wordmark-trade" x="268" y="530">PHOTOGRAPHY</text>
    </g>

    <g class="contact-block">
      <text class="holder-name" x="438" y="250">MARLOW VANCE</text>
      <text class="contact-line" x="442" y="326">+27 (0)82 555 0147</text>
      <text class="contact-line" x="442" y="380">+27 (0)31 555 0193</text>
      <text class="contact-line" x="436" y="434">marlow@marlowvance.co.za</text>
      <text class="contact-line" x="436" y="488">www.marlowvance.co.za</text>
    </g>

    <g class="wordmark wordmark-right" text-anchor="start">
      <text class="wordmark-first" x="928" y="286">MARLOW</text>
      <text class="wordmark-last" x="932" y="450">VANCE</text>
      <text class="wordmark-trade" x="936" y="530">PHOTOGRAPHY</text>
    </g>
  </svg>
</main>
</body>
</html>
```